TCH Business cards

We are a medium sized property company based in London and require a logo, Business card which reflects a professional company and incorporates our catchy name.

Our statement is (Building for the future) we like colours such as royal blue, greens and light browns but will look at anything.

Contact Information for Business Card

Tidecrest Holdings Limited
Unit 4, 3-5 Parbrook Lane
London
SE21 7QX

Web: www.tidecrestholdings.example

Email: tidecrestltd@mailbox.example

Telephone: +44-208-555-0142
Fax: +44-208-555-0187

```html
<!DOCTYPE html>
<html lang="en">
<head>
<meta charset="utf-8">
<title>Tidecrest Holdings Limited – Business Card</title>
<link rel="stylesheet" href="https://fonts.googleapis.com/css2?family=Ubuntu:wght@500;700&display=swap">
<style>
  :root {
    --backdrop: #d6d8db;
    --card-violet: #5f63a5;
    --card-green: #66c127;
    --text-cream: #e9d1aa;
    --mark-violet: #5a5ea3;
  }
  * { box-sizing: border-box; margin: 0; padding: 0; }
  html, body {
    width: 1200px; height: 1000px; overflow: hidden;
    background: var(--backdrop);
  }
  .canvas {
    position: relative; width: 1200px; height: 1000px;
    display: flex; align-items: center; justify-content: center;
  }
  .business-card {
    position: relative; width: 1050px; height: 600px;
    background: var(--card-violet);
    overflow: hidden;
    box-shadow: 0 10px 30px rgba(0,0,0,0.18);
    font-family: "Ubuntu", sans-serif;
  }
  .green-panel { position: absolute; inset: 0; width: 100%; height: 100%; }
  .brand {
    position: absolute; top: 34px; left: 826px;
    display: flex; align-items: flex-start; gap: 10px;
    color: var(--mark-violet);
    font-weight: 700; font-size: 27px; line-height: 1.08;
  }
  .brand-square {
    width: 16px; height: 16px; margin-top: 7px;
    background: var(--mark-violet);
  }
  .company-name {
    position: absolute; top: 250px; left: 110px;
    color: var(--text-cream);
    font-weight: 700; font-size: 32px; letter-spacing: 0.5px;
  }
  .contact {
    position: absolute; top: 355px; left: 190px; width: 560px;
    color: var(--text-cream);
    font-weight: 700; font-size: 21px; line-height: 1.4;
    text-align: center;
  }
  .contact .sep {
    display: inline-block; width: 12px; height: 12px;
    border-radius: 50%; background: var(--text-cream);
    margin: 0 8px; vertical-align: 1px;
  }
  .address {
    position: absolute; top: 495px; left: 190px; width: 560px;
    color: var(--text-cream);
    font-weight: 700; font-size: 22px; text-align: center;
  }
</style>
</head>
<body>
<main class="canvas">
  <section class="business-card" aria-label="Tidecrest Holdings Limited business card">
    <svg class="green-panel" viewBox="0 0 1050 600" preserveAspectRatio="none" aria-hidden="true">
      <polygon points="800,0 1050,0 1050,600 1010,600 720,165" fill="var(--card-green)"/>
    </svg>

    <div class="brand">
      <span class="brand-square"></span>
      <span class="brand-name">Tidecrest<br>Holdings<br>Limited</span>
    </div>

    <h1 class="company-name">Tidecrest Holdings Limited</h1>

    <div class="contact">
      <p>T : +44-208-555-0142<span class="sep"></span>F : +44-208-555-0187</p>
      <p>E : tidecrestltd@mailbox.example</p>
      <p>W : www.tidecrestholdings.example</p>
    </div>

    <p class="address">Unit 4, 3-5 Parbrook Lane, London SE21 7QX</p>
  </section>
</main>
</body>
</html>
```